2022 Grenache Hillside Vineyard Sketch Wine Label

Size:4"X4"
Wine: 2022 Grenache
Vineyard Name: Low Mill Vineyard
AVA: Solano County
Alcohol by Volume:15%
Volume:750ml
Must Feature a hillside vineyard on the label somehow, I picture it being a sketch but it doesn't have to be. Not looking for anything flashy or colorful but maybe a pop of color somewhere. I am not yet sure that I want to include our name, but you can try to work in "KMT" somewhere on the label if it fits the design.
The Label must include all the information listed above. The Grenache was grown in a hillside vineyard, so I wanted the label to prominently feature a hillside vineyard. You can layout the label however you see best, but the vintage and varietal should be prominent, the ABV can be in small type face but must be legible following FQD guidelines. If you are able to make the vineyard name pop as well that would be good.
You don't have to use these, but our standard fonts we use are:
For Varietal: Bianca
Secondary (vintage, AVA, Vineyard):Helvetica
ABV/Volume: PT Serif
Thank you, look forward to the results

```html
<!DOCTYPE html>
<html lang="en">
<head>
<meta charset="utf-8">
<title>KMT Grenache 2022 — Wine Label</title>
<link href="https://fonts.googleapis.com/css2?family=Cinzel:wght@400;500;600;700&family=Arimo:wght@400;700&display=swap" rel="stylesheet">
<style>
  :root{
    --wine:#8b0000;
    --ink:#111111;
    --stone:#7d7d7d;
    --rule:#c9c9c9;
    --paper:#ffffff;
    --trim:#9a9a9a;
    --sketch-light:#f1f1f1;
    --sketch-mid:#c4c4c4;
    --sketch-dark:#8a8a8a;
  }
  *{margin:0;padding:0;box-sizing:border-box;}
  html,body{width:1200px;height:690px;overflow:hidden;background:var(--paper);}
  .canvas{position:relative;width:1200px;height:690px;background:var(--paper);}

  .label{position:absolute;border:1px solid var(--trim);background:var(--paper);}
  .label--front{left:139px;top:104px;width:481px;height:481px;}
  .label--back{left:698px;top:104px;width:361px;height:481px;}

  .frame{position:absolute;border:3.5px solid var(--wine);overflow:hidden;}
  .label--front .frame{left:15px;top:15px;width:451px;height:450px;}
  .label--back .frame{left:12px;top:12px;width:336px;height:456px;}

  .center{position:absolute;left:0;right:0;text-align:center;white-space:nowrap;}

  .brand{top:36px;font-family:"Cinzel",serif;font-weight:700;font-size:49px;line-height:1;color:var(--ink);letter-spacing:-1px;}
  .varietal{top:150px;font-family:"Cinzel",serif;font-weight:700;font-size:38px;line-height:1;color:var(--ink);letter-spacing:0.5px;}
  .vintage{top:189px;display:flex;justify-content:center;align-items:center;gap:2px;}
  .vintage__rule{width:52px;height:1.5px;}
  .vintage__rule--left{background:linear-gradient(90deg,rgba(139,0,0,0),var(--wine));}
  .vintage__rule--right{background:linear-gradient(90deg,var(--wine),rgba(139,0,0,0));}
  .vintage__year{font-family:"Cinzel",serif;font-weight:600;font-size:23px;line-height:1;color:var(--wine);letter-spacing:12px;padding-left:12px;}

  .vineyard{top:265px;font-family:"Cinzel",serif;font-weight:700;font-size:20px;line-height:1;color:var(--stone);}
  .vineyard__rule{position:absolute;left:120px;width:211px;top:288px;height:1px;background:var(--rule);}
  .ava{top:290px;font-family:"Cinzel",serif;font-weight:500;font-size:14.5px;line-height:1;color:var(--stone);letter-spacing:3px;}
  .specs{top:315px;font-family:"Cinzel",serif;font-weight:600;font-size:12.5px;line-height:1;color:var(--stone);}
  .specs__divider{display:inline-block;width:1px;height:12px;background:var(--rule);margin:0 5px;vertical-align:-1px;}

  .sketch{position:absolute;left:0;right:0;bottom:0;}
  .label--front .sketch{height:113px;}
  .label--back .sketch{height:150px;}
  .sketch svg{display:block;width:100%;height:100%;}

  .producer{top:24px;font-family:"Cinzel",serif;font-weight:600;font-size:20px;line-height:23px;color:var(--ink);}
  .site{position:absolute;left:13px;width:311px;top:106px;height:37px;border-radius:19px;background:var(--wine);color:var(--paper);font-family:"Cinzel",serif;font-weight:600;font-size:19px;line-height:37px;text-align:center;white-space:nowrap;overflow:hidden;}
  .warning{position:absolute;left:17px;width:293px;top:161px;font-family:"Arimo",sans-serif;font-size:13px;line-height:15px;color:var(--ink);text-align:justify;}
  .warning__head{font-weight:700;}
  .sulfites{position:absolute;right:24px;top:255px;font-family:"Arimo",sans-serif;font-weight:700;font-size:13px;line-height:1;color:var(--ink);}
</style>
</head>
<body>
<main class="canvas">

  <section class="label label--front" aria-label="Front label">
    <div class="frame">
      <div class="center brand">KMT</div>
      <h1 class="center varietal">GRENACHE</h1>
      <div class="center vintage">
        <span class="vintage__rule vintage__rule--left"></span>
        <span class="vintage__year">2022</span>
        <span class="vintage__rule vintage__rule--right"></span>
      </div>
      <div class="center vineyard">LOW MILL VINEYARD</div>
      <div class="vineyard__rule"></div>
      <div class="center ava">SOLANO COUNTY</div>
      <div class="center specs">15%<span class="specs__divider"></span>750ML</div>
      <div class="sketch" role="img" aria-label="Pen sketch of a hillside vineyard with rows of vines leading toward rolling hills">
        <svg viewBox="0 0 451 113" preserveAspectRatio="none">
          <defs>
            <linearGradient id="hillFront" x1="0" y1="0" x2="0" y2="1">
              <stop offset="0" stop-color="var(--sketch-light)"/>
              <stop offset="0.45" stop-color="var(--sketch-mid)"/>
              <stop offset="1" stop-color="var(--sketch-dark)"/>
            </linearGradient>
          </defs>
          <rect width="451" height="113" fill="url(#hillFront)"/>
        </svg>
      </div>
    </div>
  </section>

  <section class="label label--back" aria-label="Back label">
    <div class="frame">
      <div class="center producer">PRODUCED &amp; BOTTLED BY<br>KINGSMEAD TRAILS<br>VACAVIEW CA</div>
      <div class="site">KINGSMEADTRAILS.COM</div>
      <p class="warning"><span class="warning__head">GOVERNMENT WARNING:</span> (1) According to the Surgeon General, women should not drink alcoholic beverages during pregnancy because of the risk of birth defects. (2) Consumption of alcoholic beverages impairs your ability to drive a car or operate machinery, and may cause health problems.</p>
      <div class="sulfites">CONTAINS SULFITES</div>
      <div class="sketch" role="img" aria-label="Pen sketch of a hillside vineyard with rows of vines leading toward rolling hills">
        <svg viewBox="0 0 336 150" preserveAspectRatio="none">
          <defs>
            <linearGradient id="hillBack" x1="0" y1="0" x2="0" y2="1">
              <stop offset="0" stop-color="var(--sketch-light)"/>
              <stop offset="0.45" stop-color="var(--sketch-mid)"/>
              <stop offset="1" stop-color="var(--sketch-dark)"/>
            </linearGradient>
          </defs>
          <rect width="336" height="150" fill="url(#hillBack)"/>
        </svg>
      </div>
    </div>
  </section>

</main>
</body>
</html>
```